Bright-loop designs Business Card

embroidery printing

Target Market(s)

Businesses and public

Industry/Entity Type

Business

Contact Information for Business Card

Front of card..... Bright-loop designs .... Corin Maltby..... 868 512-7361.... Email... bright_loopdesigns@mailbrook.net

Back of card..... Bright-loop designs embroidery & artwork

Colors
000000

```html
<!DOCTYPE html>
<html lang="en">
<head>
<meta charset="utf-8">
<title>Bright-loop designs – Business Card</title>
<link rel="stylesheet" href="https://fonts.googleapis.com/css2?family=Questrial&family=Michroma&display=swap">
<style>
  :root {
    --page: #d9d9d9;
    --brand-red: #a32a22;
    --brand-red-soft: #b54a40;
    --ink: #000000;
    --paper: #ffffff;
    --rule: #1a1a1a;
  }
  * { box-sizing: border-box; margin: 0; padding: 0; }
  html, body { width: 1200px; height: 900px; overflow: hidden; }
  body {
    background: var(--page);
    font-family: "Questrial", sans-serif;
    position: relative;
  }
  .card {
    position: absolute;
    left: 250px;
    width: 700px;
    height: 400px;
    border-radius: 28px;
    overflow: hidden;
    box-shadow: 0 8px 24px rgba(0,0,0,0.25);
  }

  /* Back of card */
  .card-back { top: 40px; background: var(--brand-red); }
  .card-back .backdrop-ornament {
    position: absolute;
    left: 170px; top: 150px;
    width: 520px; height: 260px;
    border-radius: 160px 160px 0 0;
    background: var(--brand-red-soft);
    opacity: 0.55;
  }
  .card-back .brand-block {
    position: absolute;
    left: 0; right: 0; top: 120px;
    text-align: center;
  }
  .card-back .brand-name {
    font-size: 62px;
    color: var(--ink);
    letter-spacing: 1px;
    line-height: 1;
  }
  .card-back .tagline {
    margin-top: 18px;
    font-family: "Michroma", sans-serif;
    font-size: 20px;
    color: var(--ink);
    letter-spacing: 2px;
    text-transform: uppercase;
  }

  /* Front of card */
  .card-front { top: 470px; background: var(--paper); }
  .card-front .brand-name {
    position: absolute;
    left: 48px; top: 70px;
    font-size: 48px;
    color: var(--ink);
    line-height: 1;
  }
  .card-front .top-rule {
    position: absolute;
    left: 420px; right: 0; top: 112px;
    border-top: 2px solid var(--rule);
  }
  .card-front .holder {
    position: absolute;
    left: 0; top: 206px;
    display: flex; align-items: center;
    width: 460px;
  }
  .card-front .holder::before {
    content: ""; width: 40px; border-top: 2px solid var(--rule); margin-right: 10px;
  }
  .card-front .holder-name {
    font-size: 30px;
    color: var(--brand-red);
    letter-spacing: 2px;
    text-transform: uppercase;
  }
  .card-front .contact-band {
    position: absolute;
    left: 0; right: 0; bottom: 0;
    height: 92px;
    background: var(--ink);
    padding: 18px 0 0 48px;
    color: var(--paper);
    font-size: 19px;
    line-height: 28px;
  }
  .contact-line { display: flex; align-items: center; gap: 12px; }
  .contact-line svg { width: 16px; height: 16px; flex: none; }
  .card-front .corner-ornament {
    position: absolute;
    right: 0; bottom: 40px;
    width: 330px; height: 150px;
    background: var(--brand-red);
    border-radius: 150px 0 0 0;
  }
</style>
</head>
<body>

  <section class="card card-back">
    <div class="backdrop-ornament" role="img" aria-label="Faint decorative flourish in lighter red"></div>
    <div class="brand-block">
      <div class="brand-name">Bright-loop designs</div>
      <div class="tagline">Embroidery &amp; Artwork</div>
    </div>
  </section>

  <section class="card card-front">
    <div class="brand-name">Bright-loop designs</div>
    <div class="top-rule"></div>
    <div class="holder"><span class="holder-name">Corin Maltby</span></div>
    <div class="corner-ornament" role="img" aria-label="Red decorative scroll ornament"></div>
    <div class="contact-band">
      <div class="contact-line">
        <svg viewBox="0 0 16 16" aria-hidden="true"><rect x="4" y="1" width="8" height="14" rx="1.5" fill="none" stroke="#a32a22" stroke-width="1.6"/><circle cx="8" cy="12.5" r="0.9" fill="#a32a22"/></svg>
        <span>868 512-7361</span>
      </div>
      <div class="contact-line">
        <svg viewBox="0 0 16 16" aria-hidden="true"><rect x="1.5" y="3.5" width="13" height="9" fill="none" stroke="#a32a22" stroke-width="1.6"/><path d="M1.5 3.5 L8 9 L14.5 3.5" fill="none" stroke="#a32a22" stroke-width="1.6"/></svg>
        <span>bright_loopdesigns@mailbrook.net</span>
      </div>
    </div>
  </section>

</body>
</html>
```